Greta Polanski Consulting

I am starting my own business and want to have a business card that stands out from the rest. Class is the word i use to describe what i would like to my card to look like.

I see my card as vibrant red card with rounded edges. mat finish
Centered scripted writing
large scripted font: Greta Polanski, smaller font & not scripted: Consulting, next line 0438157226, next line greta@polanskihome.com.au

i have now left 2 email message for the design of my card. Family is spelt wrong on the card. this needs to be correct and finial proof sent though!!! before i can download and approve
Greta

Target Market(s)

Real Estate Professionals

Industry/Entity Type

Business

Contact Information for Business Card

Greta Polanski
Consulting
0438 157 226
greta@polanskihome.com.au

Logo Text

no logo

Requirements
Must have
• must have rounded edges

```html
<!DOCTYPE html>
<html lang="en">
<head>
<meta charset="UTF-8">
<title>Greta Polanski Consulting – Business Card</title>
<link rel="stylesheet" href="https://fonts.googleapis.com/css2?family=Pinyon+Script&family=Cinzel:wght@400&family=Questrial&display=swap">
<style>
  :root {
    --backdrop: #e9e6e3;
    --card-red-light: #d81e27;
    --card-red: #c01a22;
    --card-red-deep: #9c141b;
    --ink: #120506;
    --silver: #e8dcd6;
    --icon-fill: #e6d3cb;
  }
  * { margin: 0; padding: 0; box-sizing: border-box; }
  html, body {
    width: 1200px;
    height: 900px;
    overflow: hidden;
    background: var(--backdrop);
  }
  .canvas {
    position: relative;
    width: 1200px;
    height: 900px;
    display: flex;
    align-items: center;
    justify-content: center;
  }
  .business-card {
    position: relative;
    width: 900px;
    height: 550px;
    border-radius: 34px;
    background: linear-gradient(160deg, var(--card-red-light) 0%, var(--card-red) 45%, var(--card-red-deep) 100%);
    box-shadow: 0 14px 30px rgba(0, 0, 0, 0.22);
  }
  .card-name {
    position: absolute;
    left: 0;
    right: 0;
    top: 110px;
    text-align: center;
    padding-left: 70px;
    font-family: "Pinyon Script", cursive;
    font-size: 104px;
    line-height: 1;
    color: var(--ink);
    white-space: nowrap;
  }
  .card-tagline {
    position: absolute;
    left: 0;
    right: 0;
    top: 245px;
    text-align: center;
    padding-right: 30px;
    font-family: "Cinzel", serif;
    font-size: 30px;
    letter-spacing: 2px;
    color: var(--silver);
  }
  .contact-list {
    position: absolute;
    left: 470px;
    top: 330px;
    list-style: none;
    font-family: "Questrial", sans-serif;
    font-size: 25px;
    letter-spacing: 1px;
    color: var(--ink);
  }
  .contact-item {
    display: flex;
    align-items: center;
    gap: 16px;
    height: 46px;
  }
  .contact-item + .contact-item { margin-top: 20px; }
  .contact-icon {
    width: 22px;
    height: 22px;
    flex: none;
  }
</style>
</head>
<body>
<main class="canvas">
  <section class="business-card" aria-label="Business card">
    <h1 class="card-name">Greta Polanski</h1>
    <p class="card-tagline">Consulting</p>
    <ul class="contact-list">
      <li class="contact-item">
        <svg class="contact-icon" viewBox="0 0 22 22" aria-hidden="true">
          <circle cx="11" cy="11" r="9.5" fill="none" stroke="var(--icon-fill)" stroke-width="1.6"/>
          <path d="M8 6.5c-.8.4-1.3 1.3-1 2.4.6 2.4 2.7 4.7 5.2 5.9 1 .5 2 .1 2.4-.6l-1.6-1.6-1.1.6c-1-.6-2-1.6-2.6-2.7l.6-1.1L8.3 6.5z" fill="var(--icon-fill)"/>
        </svg>
        <span>0438 157 226</span>
      </li>
      <li class="contact-item">
        <svg class="contact-icon" viewBox="0 0 22 22" aria-hidden="true">
          <text x="11" y="17" text-anchor="middle" font-family="Questrial, sans-serif" font-size="19" fill="var(--icon-fill)">@</text>
        </svg>
        <span>greta@polanskihome.com.au</span>
      </li>
    </ul>
  </section>
</main>
</body>
</html>
```